Information Rack Card for our Cedar Hollow Perks Program

This 2 sided rack card provides information to guest about our Rewards program. We have relaunched it this year with new logo and new logo - Treat Your Stay- this needs to be modern and informative yet a marketing piece.

I have attached the one we currently are using

Program Details
Silver status on our rewards program, a guest needs to sign up using their birth month and day. Guest enrolled will receive the benefits of the Silver Status immediately. To reach Gold status a guest must be enrolled and stayed with us 10 nights or spent $1000 with us in a given year. Once they reach Gold Status, they remain at Gold for the remainder of that year and the following year. To become (or remain) Gold, they need to meet requirements each year to be Gold the Following year.
Silver Benefits:
Earn 100 points on every dollar spent on an eligible stay.
Birthday email with discount offer and free gift.
Discounts to local restaurants, wineries and attractions.
Signup gift and arrival gift with each stay.

Gold Benefits:
Earn 100 points plus 20 bonus points on every dollar spent on an eligible stay.
Special Rewards Member Rate
Arrival Gift each time they stay.
Bottle of water at Check In
Special Check in Point at front desk for Gold Members
Free upgrade based on availability at Checkin
Gold member monthly special offer email

Target Market(s)

Guest and repeat guest to get them to sign up for the loyaltty progrm

Industry/Entity Type

Hospitality

Requirements
Must have
• must have the descriptions listed in the project description about Silver/Gold.
• Start earning points TODAY for every qualified purchase with Cedar Hollow Lodges.
• To Redeem call 1-800-555-0148
• For more information visit CedarHollowPerks.com
Nice to have
• Hotel logos

```html
<!DOCTYPE html>
<html lang="en">
<head>
<meta charset="utf-8">
<title>Cedar Hollow Perks – Rack Card</title>
<link href="https://fonts.googleapis.com/css2?family=Montserrat+Alternates:wght@300;400;600;700;800&display=swap" rel="stylesheet">
<style>
  :root{
    --backdrop:#959595;
    --green-dark:#2e6a06;
    --green-light:#5bb30a;
    --green-text:#2e6a06;
    --tick:#4fae2a;
    --ink:#1c1c1c;
    --body:#333;
    --bar:#4a4a4a;
    --pill-silver:#e2e2e2;
    --pill-gold-a:#f4c067;
    --pill-gold-b:#e49a2c;
    --badge:#c9c9c9;
    --white:#fff;
  }
  *{margin:0;padding:0;box-sizing:border-box}
  html,body{width:1200px;height:1200px;overflow:hidden}
  body{background:var(--backdrop);position:relative;font-family:"Montserrat Alternates",sans-serif;color:var(--ink)}

  .card{position:absolute;background:var(--white);overflow:hidden}
  .card--front{left:193px;top:197px;width:361px;height:770px}
  .card--back{left:715px;top:197px;width:358px;height:759px}
  .card__shapes{position:absolute;inset:0;width:100%;height:100%}

  .photo{position:absolute;left:0;top:0;width:361px;height:425px;
    background:linear-gradient(180deg,#8fc0e8 0%,#c9dff0 28%,#4f7f3a 45%,#6b6b5e 58%,#58b9d6 72%,#7ccbe0 100%)}

  .headline{position:absolute;left:21px;top:421px;color:var(--white);font-weight:700;font-size:44px;line-height:45px;letter-spacing:-.5px}
  .tagline{position:absolute;left:21px;top:517px;color:var(--white);font-weight:300;font-size:33px;line-height:40px;white-space:nowrap}

  .intro{position:absolute;left:17px;top:604px;width:330px;font-weight:700;font-size:13.3px;line-height:16px;color:var(--ink)}

  .redeem{position:absolute;font-weight:700;white-space:nowrap}
  .redeem__label{display:block;font-size:18px;line-height:21px;color:#2a2a2a}
  .redeem__phone{display:block;font-size:18px;line-height:22px;color:var(--green-text)}
  .card--front .redeem{left:19px;top:667px}
  .card--back .redeem{left:19px;top:657px}

  .brand{position:absolute;display:flex;align-items:center;gap:5px;font-weight:800;font-size:12px;line-height:14px;color:var(--green-dark);white-space:nowrap}
  .brand__mark{width:11px;height:11px;background:var(--green-light);flex:none}
  .card--front .brand{right:16px;top:685px}
  .card--back .brand{right:16px;top:675px}

  .info-bar{position:absolute;left:0;width:100%;height:29px;background:var(--bar);color:var(--white);font-weight:600;font-size:11px;line-height:29px;text-align:center;white-space:nowrap}
  .card--front .info-bar{top:726px}
  .card--back .info-bar{top:716px}

  .program{position:absolute;left:18px;top:24px;width:322px;color:var(--white);font-size:10px;line-height:12.2px;text-align:justify;font-weight:400}

  .tier-pill{position:absolute;left:18px;height:19px;padding:0 8px;border-radius:3px;font-weight:800;font-size:10px;line-height:19px;letter-spacing:.4px;text-transform:uppercase;color:#3a3a3a;white-space:nowrap}
  .tier-pill--silver{top:200px;background:var(--pill-silver)}
  .tier-pill--gold{top:332px;background:linear-gradient(180deg,var(--pill-gold-a),var(--pill-gold-b));color:#4a3210}

  .benefits{position:absolute;left:18px;width:320px;list-style:none;font-size:10.3px;line-height:19.2px;color:var(--body)}
  .benefits li{display:flex;align-items:flex-start;gap:8px}
  .benefits svg{flex:none;width:8px;height:8px;margin-top:5.6px}
  .benefits--silver{top:232px}
  .benefits--gold{top:360px}

  .partners{position:absolute;left:18px;top:581px;width:322px;height:50px;display:flex;align-items:center;justify-content:space-between}
  .partner-badge{width:50px;height:50px;border-radius:50%;background:var(--badge)}
  .partner-name{font-weight:700;font-size:11px;line-height:13px;color:var(--green-dark);text-align:center;width:110px}
  .partner-inn{display:flex;align-items:center;gap:5px;font-weight:700;font-size:11px;line-height:13px;color:#1d6b4a;white-space:nowrap}
  .partner-inn__mark{width:11px;height:11px;background:#1d6b4a}
</style>
</head>
<body>

<section class="card card--front" aria-label="Rack card front">
  <div class="photo" role="img" aria-label="Photo of families enjoying the lodge outdoor pool on a sunny day"></div>
  <svg class="card__shapes" viewBox="0 0 452 962" preserveAspectRatio="none" aria-hidden="true">
    <polygon points="0,417 250,500 452,472 452,728 0,710" fill="#5bb30a"/>
    <polygon points="24,490 452,530 452,709 0,709 0,640" fill="#2e6a06"/>
  </svg>
  <h1 class="headline">Treat Your<br>Stay</h1>
  <p class="tagline">Save Earn Reedem</p>
  <p class="intro">Start earning points TODAY for every qualified purchase with Cedar Hollow Lodges.</p>
  <p class="redeem"><span class="redeem__label">To Redeem call</span><span class="redeem__phone">1-800-555-0148</span></p>
  <div class="brand"><span class="brand__mark"></span><span>Cedar Hollow Perks</span></div>
  <div class="info-bar">For more information visit CedarHollowPerks.com</div>
</section>

<section class="card card--back" aria-label="Rack card back">
  <svg class="card__shapes" viewBox="0 0 447 949" preserveAspectRatio="none" aria-hidden="true">
    <polygon points="0,180 447,180 447,277 270,216 12,226" fill="#5bb30a"/>
    <polygon points="0,0 447,0 447,175 437,232 265,214 0,185" fill="#2e6a06"/>
  </svg>
  <p class="program">Silver status on our rewards program, a guest needs to sign up using their birth month and day. Guest enrolled will receive the benefits of the Silver Status immediately. To reach Gold status a guest must be enrolled and stayed with us 10 nights or spent $1000 with us in a given year. Once they reach Gold Status, they remain at Gold for the remainder of that year and the following year. To become (or remain) Gold, they need to meet requirements each year to be Gold the Following year.</p>

  <div class="tier-pill tier-pill--silver">Silver Benefits</div>
  <ul class="benefits benefits--silver">
    <li><svg viewBox="0 0 10 10"><circle cx="5" cy="5" r="5" fill="#4fae2a"/><path d="M2.6 5.2 4.3 6.8 7.4 3.5" stroke="#fff" stroke-width="1.4" fill="none"/></svg><span>Earn 100 points on every dollar spent on an eligible stay.</span></li>
    <li><svg viewBox="0 0 10 10"><circle cx="5" cy="5" r="5" fill="#4fae2a"/><path d="M2.6 5.2 4.3 6.8 7.4 3.5" stroke="#fff" stroke-width="1.4" fill="none"/></svg><span>Birthday email with discount offer and free gift.</span></li>
    <li><svg viewBox="0 0 10 10"><circle cx="5" cy="5" r="5" fill="#4fae2a"/><path d="M2.6 5.2 4.3 6.8 7.4 3.5" stroke="#fff" stroke-width="1.4" fill="none"/></svg><span>Discounts to local restaurants, wineries and attractions.</span></li>
    <li><svg viewBox="0 0 10 10"><circle cx="5" cy="5" r="5" fill="#4fae2a"/><path d="M2.6 5.2 4.3 6.8 7.4 3.5" stroke="#fff" stroke-width="1.4" fill="none"/></svg><span>Signup gift and arrival gift with each stay.</span></li>
  </ul>

  <div class="tier-pill tier-pill--gold">Gold Benefits</div>
  <ul class="benefits benefits--gold">
    <li><svg viewBox="0 0 10 10"><circle cx="5" cy="5" r="5" fill="#4fae2a"/><path d="M2.6 5.2 4.3 6.8 7.4 3.5" stroke="#fff" stroke-width="1.4" fill="none"/></svg><span>Earn 100 points plus 20 bonus points on every dollar<br>spent on an eligible stay.</span></li>
    <li><svg viewBox="0 0 10 10"><circle cx="5" cy="5" r="5" fill="#4fae2a"/><path d="M2.6 5.2 4.3 6.8 7.4 3.5" stroke="#fff" stroke-width="1.4" fill="none"/></svg><span>Birthday email with discount offer and free gift.</span></li>
    <li><svg viewBox="0 0 10 10"><circle cx="5" cy="5" r="5" fill="#4fae2a"/><path d="M2.6 5.2 4.3 6.8 7.4 3.5" stroke="#fff" stroke-width="1.4" fill="none"/></svg><span>Discounts to local restaurants, wineries and attractions.</span></li>
    <li><svg viewBox="0 0 10 10"><circle cx="5" cy="5" r="5" fill="#4fae2a"/><path d="M2.6 5.2 4.3 6.8 7.4 3.5" stroke="#fff" stroke-width="1.4" fill="none"/></svg><span>Special Rewards Member Rate</span></li>
    <li><svg viewBox="0 0 10 10"><circle cx="5" cy="5" r="5" fill="#4fae2a"/><path d="M2.6 5.2 4.3 6.8 7.4 3.5" stroke="#fff" stroke-width="1.4" fill="none"/></svg><span>Arrival Gift each time they stay.</span></li>
    <li><svg viewBox="0 0 10 10"><circle cx="5" cy="5" r="5" fill="#4fae2a"/><path d="M2.6 5.2 4.3 6.8 7.4 3.5" stroke="#fff" stroke-width="1.4" fill="none"/></svg><span>Bottle of water at Check In</span></li>
    <li><svg viewBox="0 0 10 10"><circle cx="5" cy="5" r="5" fill="#4fae2a"/><path d="M2.6 5.2 4.3 6.8 7.4 3.5" stroke="#fff" stroke-width="1.4" fill="none"/></svg><span>Special Check in Point at front desk for Gold Members</span></li>
    <li><svg viewBox="0 0 10 10"><circle cx="5" cy="5" r="5" fill="#4fae2a"/><path d="M2.6 5.2 4.3 6.8 7.4 3.5" stroke="#fff" stroke-width="1.4" fill="none"/></svg><span>Free upgrade based on availability at Checkin</span></li>
    <li><svg viewBox="0 0 10 10"><circle cx="5" cy="5" r="5" fill="#4fae2a"/><path d="M2.6 5.2 4.3 6.8 7.4 3.5" stroke="#fff" stroke-width="1.4" fill="none"/></svg><span>Gold member monthly special offer email</span></li>
  </ul>

  <div class="partners">
    <div class="partner-badge" role="img" aria-label="Partner award badge"></div>
    <div class="partner-name">Maple Falls Waterpark Resort</div>
    <div class="partner-inn"><span class="partner-inn__mark"></span><span>Brookside Inn</span></div>
  </div>

  <p class="redeem"><span class="redeem__label">To Redeem call</span><span class="redeem__phone">1-800-555-0148</span></p>
  <div class="brand"><span class="brand__mark"></span><span>Cedar Hollow Perks</span></div>
  <div class="info-bar">For more information visit CedarHollowPerks.com</div>
</section>

</body>
</html>
```